Re-design and craft the perfect CV platform

We are building a CV-based platform designed to connect employees and employers, with a strong focus on individual users. As we're just starting out, we're looking to have our platform and logo redesigned to better reflect our vision
https://app.lumoshire.com/
Colors like in the logo attached
#87C032 #6A6E71 #618930 - also you can add more colors if you like.
https://app.lumoshire.com/dashboard - This page would be nice if you plan it, like personal Bio dashboard. Attached picture (Dashboard wanted) one idea from how we would like to be, but we are open for new professional ideas/solutions.
https://app.lumoshire.com/posts - On this page we want to be showed the jobs posted. Attached one picture about our idea (jobs page wanted)
https://app.lumoshire.com/profile - design something nice.
Only Photoshop, Illustrator or Figma
Other pictures from the app attached (as looking right now)

Target Market(s)

Job seekers, HR, Recruiters

Industry/Entity Type

HR Tech

Number of Pages Required

5+ page

Colors
00AB8E
00BBA5
67D7C9
C6EFE9
E9F9F6

```html
<!DOCTYPE html>
<html lang="en">
<head>
<meta charset="utf-8">
<title>Lumoshire – Profile</title>
<link href="https://fonts.googleapis.com/css2?family=Outfit:wght@300;400;500;600&display=swap" rel="stylesheet">
<style>
:root{
  --green:#87C032;
  --green-dark:#618930;
  --green-pale:#E3F1CC;
  --grey:#6A6E71;
  --grey-text:#5a5e61;
  --grey-light:#dcdcdc;
  --page:#f4f4f4;
  --card:#ffffff;
}
*{box-sizing:border-box;margin:0;padding:0}
html,body{width:1200px;height:712px;overflow:hidden}
body{font-family:"Outfit",sans-serif;background:var(--page);color:var(--grey-text);position:relative;font-weight:300}
.topbar{position:absolute;left:0;top:0;width:1200px;height:59px;background:var(--card)}
.brand{position:absolute;left:23px;top:18px;display:flex;align-items:center;gap:7px;font-weight:600;font-size:20px;color:var(--green)}
.brand-dot{width:14px;height:14px;border-radius:50%;background:var(--green)}
.nav{position:absolute;top:20px;font-size:15px;color:var(--grey);display:flex;align-items:center;gap:6px;font-weight:400}
.nav svg{fill:var(--grey)}
.badge{position:absolute;left:9px;top:-2px;width:9px;height:9px;border-radius:50%;background:#e0403a;color:#fff;font-size:6px;text-align:center;line-height:9px}
.card{position:absolute;background:var(--card);border-radius:14px}
.profile{left:27px;top:83px;width:230px;height:300px;border-bottom:4px solid var(--green)}
.edit{position:absolute;right:18px;top:20px;stroke:var(--grey);fill:none}
.avatar-ring{position:absolute;left:60px;top:23px;width:110px;height:110px;border-radius:50%;border:2px solid var(--green);padding:7px}
.avatar{width:100%;height:100%;border-radius:50%;background:radial-gradient(circle at 50% 45%,#e8b48f 0 30%,#5cb85c 31%)}
.name{position:absolute;top:146px;width:100%;text-align:center;font-size:19px;font-weight:400;color:var(--grey)}
.facts{position:absolute;left:22px;top:182px;font-size:11px;border-collapse:collapse}
.facts th{text-align:left;font-weight:600;padding:0 18px 3.5px 0;color:var(--grey-text)}
.facts td{padding:0 0 3.5px}
.main{left:269px;top:85px;width:664px;height:595px;padding:34px 40px 0 43px}
h2{font-size:19px;font-weight:500;color:var(--grey);text-transform:uppercase;letter-spacing:.1px;line-height:1}
.main p{font-size:11.2px;line-height:15px;margin:10px 0 0}
.main h2+.role{margin-top:10px}
.section{margin-top:22px}
.role{font-size:11px;font-weight:600;line-height:15px}
ul.dots{list-style:none;font-size:11.2px}
ul.dots li{position:relative;padding-left:12px;line-height:15px}
ul.dots li::before{content:"";position:absolute;left:1px;top:6px;width:3.5px;height:3.5px;border-radius:50%;background:var(--green)}
.duties{margin-top:8px}
.duties li{margin-bottom:7.5px}
.cols{display:flex;margin-top:15px}
.cols>div{width:310px}
.cols ul{margin-top:12px}
.tabs{position:absolute;left:45px;top:454px;display:flex;gap:6px}
.tab{height:29px;padding:0 16px;border-radius:15px;background:var(--grey-light);font-size:11.2px;font-weight:500;line-height:29px;color:var(--grey-text)}
.tab.active{background:var(--green-pale);color:var(--green)}
.side{left:945px;width:230px;padding:22px 25px}
.side h3{font-size:19px;font-weight:500;color:var(--grey);display:flex;align-items:center;gap:6px}
.side h3 svg{stroke:var(--grey);fill:none}
.side .degree{font-size:11px;font-weight:600;margin-top:6px;line-height:15px}
.side p{font-size:11px;line-height:16px;margin-top:2px}
.side ul{margin-top:8px;font-size:11px}
.side ul.dots li{line-height:16.5px;padding-left:10px}
.lang{display:grid;grid-template-columns:48px 100px 35px;column-gap:0;align-items:center;font-size:11px;row-gap:2px;margin-top:6px}
.bar{height:3px;background:var(--grey-light);border-radius:2px;overflow:hidden}
.bar span{display:block;height:100%;background:var(--green)}
.lang .pct{padding-left:11px}
</style>
</head>
<body>
<header class="topbar">
  <div class="brand"><span class="brand-dot"></span>Lumoshire</div>
  <div class="nav" style="left:963px"><svg width="13" height="11" viewBox="0 0 13 11"><rect x="0" y="3" width="13" height="8" rx="1.5"/><rect x="4" y="0.5" width="5" height="3" rx="1" fill="none" stroke="#6A6E71" stroke-width="1.2"/></svg>Jobs</div>
  <div class="nav" style="left:1047px"><svg width="11" height="13" viewBox="0 0 11 13"><path d="M1 0h6l4 4v8a1 1 0 0 1-1 1H1a1 1 0 0 1-1-1V1a1 1 0 0 1 1-1z"/><rect x="3" y="7" width="5" height="1" fill="#fff"/><rect x="3" y="9" width="5" height="1" fill="#fff"/></svg>CV</div>
  <div class="nav" style="left:1123px"><svg width="14" height="15" viewBox="0 0 14 15"><path d="M7 1a4 4 0 0 1 4 4v4l2 2H1l2-2V5a4 4 0 0 1 4-4z"/><circle cx="7" cy="13" r="1.8"/></svg><span class="badge">1</span></div>
  <div class="nav" style="left:1161px"><svg width="13" height="14" viewBox="0 0 13 14"><circle cx="6.5" cy="4" r="3.5"/><path d="M0 14a6.5 5.5 0 0 1 13 0z"/></svg></div>
</header>

<section class="card profile">
  <svg class="edit" width="15" height="15" viewBox="0 0 15 15" stroke-width="1.2"><path d="M2 13l1-4 7.5-7.5 3 3L6 12z"/></svg>
  <div class="avatar-ring"><div class="avatar" role="img" aria-label="Profile photo of the candidate"></div></div>
  <div class="name">Martin Hale</div>
  <table class="facts">
    <tr><th>Phone</th><td>+457 5550 1234</td></tr>
    <tr><th>Email</th><td>info@martinhale.com</td></tr>
    <tr><th>Age</th><td>28</td></tr>
    <tr><th>Sex</th><td>Male</td></tr>
    <tr><th>Address</th><td>Some goes address here</td></tr>
  </table>
</section>

<main class="card main">
  <h2>Personal Statement</h2>
  <p>Efficient driver with 10 years’ experience safely transporting people and goods. Expert in planning delivery routes and schedules, interpreting maps, and analysing traffic trends to determine the fastest routes. Ready to leverage soft skills like emotional intelligence and hard skills in implementing innovative delivery systems to xyz.</p>
  <div class="section">
    <h2>Work Experience</h2>
    <div class="role">Fernway Groceries, York<br>Dispatch Driver, Dec 2018 – Present</div>
    <ul class="dots duties">
      <li>Update vehicle log detailing duty and driving hours as per DfT standards, and prepare them in print.</li>
      <li>Read maps and analyse traffic trends to identify the fastest routes, saving the company over 26 hours a month</li>
      <li>Execute 35 deliveries a day, driving pickups and vans carrying loads valued £12K+ pounds without damage to the transported goods</li>
      <li>Conduct daily interior and exterior cleaning and general preventive maintenance on vehicles</li>
    </ul>
  </div>
  <div class="cols">
    <div>
      <h2>Key Skills</h2>
      <ul class="dots">
        <li>Route optimisation</li><li>Delivery, collections, and returns</li><li>Safety regulations</li><li>Onboarding new hires</li><li>Vehicle maintenance</li><li>Loading and unloading</li>
      </ul>
    </div>
    <div>
      <h2>Hobbies &amp; Interests</h2>
      <ul class="dots">
        <li>Reading newspapers</li><li>Playing music</li><li>Watching sports</li><li>Going go-karting</li>
      </ul>
    </div>
  </div>
  <nav class="tabs">
    <span class="tab">Job post</span>
    <span class="tab active">Applied Jobs</span>
    <span class="tab">Saved jobs</span>
  </nav>
</main>

<section class="card side" style="top:83px;height:140px">
  <h3>Education <svg width="11" height="11" viewBox="0 0 15 15" stroke-width="1.5"><path d="M2 13l1-4 7.5-7.5 3 3L6 12z"/></svg></h3>
  <div class="degree">Bachelours In Computer engineering</div>
  <p>Just High School and Universirty<br>August 2019 to July 2024</p>
</section>

<section class="card side" style="top:232px;height:127px">
  <h3>Driver Licence <svg width="11" height="11" viewBox="0 0 15 15" stroke-width="1.5"><path d="M2 13l1-4 7.5-7.5 3 3L6 12z"/></svg></h3>
  <ul class="dots"><li>Valid Ohio Driver's License</li><li>Taxicab &amp; Chauffeurs Driving Training - 2018</li></ul>
</section>

<section class="card side" style="top:369px;height:194px">
  <h3>Skills <svg width="11" height="11" viewBox="0 0 15 15" stroke-width="1.5"><path d="M2 13l1-4 7.5-7.5 3 3L6 12z"/></svg></h3>
  <ul class="dots">
    <li>Clean driving record</li><li>Traffic patterns familiarity</li><li>Valid Ohio Driver's License</li><li>Passenger assistance</li><li>Road regulations knowledge</li><li>Organization and time management</li>
  </ul>
</section>

<section class="card side" style="top:572px;height:108px;padding-top:18px">
  <h3>Language <svg width="11" height="11" viewBox="0 0 15 15" stroke-width="1.5"><path d="M2 13l1-4 7.5-7.5 3 3L6 12z"/></svg></h3>
  <div class="lang">
    <span>Roman</span><div class="bar"><span style="width:56%"></span></div><span class="pct">65%</span>
    <span>Magyar</span><div class="bar"><span style="width:100%"></span></div><span class="pct">100%</span>
    <span>Angol</span><div class="bar"><span style="width:84%"></span></div><span class="pct">80%</span>
  </div>
</section>
</body>
</html>
```